Consulting, Investors, Joint Venture Website

Founded in April 2018, Marendo Advisers Limited (MAL) is an advisory consulting firm specializing in engaging investors in business ventures in Tanzania.
With extensive experience in construction, energy, oil and gas and the legal professions, our team assembles our expertise that allows foreign investors to set foot and flourish in the Tanzanian market.
MAL is locally owned, founded and registered. Our shareholders are cultured Tanzanian citizens with extensive corporate experience in South Africa, Tanzania, United Kingdom and the United States.

Our mission is to provide responsive and unrivalled professional advice from learned and experienced professionals versed in the local market, with an understanding of the cultural and logistical challenges faced by foreign investors.

Our vision is to provide a complete investor’s package that initiates with company registration, compliance and documentation services and ultimately operational facilitation services.

Target Market(s)

Foreign Investors, International companies

Industry/Entity Type

Business Consultant

Number of Pages Required

5+ page

Requirements
Must have
• It will be 5 pages - Home, About Us, Services, Portfolio, Contact Us
Nice to have
• if it can look like https://www.vq-sample.com/
• or https://www.torvell.com or http://www.bramwickpoint.com/

```html
<!DOCTYPE html>
<html lang="en">
<head>
<meta charset="utf-8">
<title>Marendo Advisers Limited</title>
<link rel="stylesheet" href="https://fonts.googleapis.com/css2?family=Audiowide&family=Montserrat:wght@400;500;600;700&family=Open+Sans:wght@400;600&display=swap">
<style>
:root{
  --blue:#0f55a6;
  --orange:#f7941d;
  --navy:#2c3e50;
  --ink:#222;
  --muted:#777;
  --light:#f6f6f6;
  --line:#cfcfcf;
  --white:#fff;
}
*{box-sizing:border-box;margin:0;padding:0}
html,body{width:1200px;height:2211px;overflow:hidden}
body{position:relative;font-family:"Open Sans",Arial,sans-serif;color:var(--ink);background:var(--white)}
.abs{position:absolute}

/* header */
.site-header{position:absolute;left:0;top:0;width:1200px;height:58px;background:var(--blue)}
.brand{position:absolute;left:0;top:0;width:408px;height:58px;background:var(--white);display:flex;align-items:center;padding-left:160px;gap:10px}
.brand-mark{width:26px;height:26px;background:var(--blue)}
.brand-name{font-family:"Montserrat",sans-serif;font-weight:700;font-size:19px;color:var(--blue);letter-spacing:.5px}
.main-nav a{position:absolute;top:21px;font-family:"Montserrat",sans-serif;font-size:11px;font-weight:600;color:var(--white);text-decoration:none;transform:translateX(-50%)}

/* hero */
.hero{position:absolute;left:0;top:58px;width:1200px;height:489px}
.hero-photo{position:absolute;inset:0;background:radial-gradient(ellipse at 50% 45%,#4a4540 0%,#2b2826 55%,#1a1817 100%)}
.hero-title{position:absolute;left:0;width:1200px;top:150px;text-align:center;font-family:"Audiowide",sans-serif;font-size:29px;line-height:38px;color:var(--white);letter-spacing:1px;text-transform:uppercase}
.hero-text{position:absolute;left:0;width:1200px;top:257px;text-align:center;font-size:14px;line-height:19px;color:#eee}
.btn{position:absolute;top:343px;height:44px;display:flex;align-items:center;justify-content:center;font-family:"Montserrat",sans-serif;font-weight:600;font-size:13px;color:var(--white)}
.btn-case{left:441px;width:156px;background:var(--orange)}
.btn-services{left:604px;width:155px;border:1px solid var(--white)}

/* about */
.about{position:absolute;left:0;top:547px;width:1200px;height:333px;background:var(--light);overflow:hidden;border-bottom:3px solid #e4e4e4}
.section-title{position:absolute;left:0;width:1200px;text-align:center;font-family:"Montserrat",sans-serif;font-weight:600;font-size:17px;color:var(--ink)}
.about-text{position:absolute;left:181px;width:838px;top:97px;text-align:center;font-size:12px;line-height:17.5px;color:var(--muted)}
.about-more{position:absolute;left:0;width:1200px;top:162px;text-align:center;font-family:"Montserrat",sans-serif;font-size:13px;font-weight:500;color:var(--blue)}
.device{position:absolute;top:197px;width:165px;height:160px;border:1.5px solid #999;border-radius:18px;background:var(--white)}
.device-cam{position:absolute;left:48px;top:18px;width:6px;height:6px;border:1px solid #888;border-radius:50%}
.device-speaker{position:absolute;left:72px;top:19px;width:24px;height:5px;border:1px solid #888;border-radius:3px}
.device-screen{position:absolute;left:10px;right:10px;top:44px;bottom:-2px;border:1.5px solid #999;border-bottom:none;display:flex;align-items:flex-start;justify-content:center;padding-top:33px;font-family:"Montserrat",sans-serif;font-size:14px;font-weight:500}

/* services */
.services{position:absolute;left:0;top:880px;width:1200px;height:619px}
.service-label{position:absolute;top:110px;font-size:12px;color:#555;transform:translateX(-50%);white-space:nowrap}
.service-label.side{transform:none;text-align:right;width:200px}
.service-node{position:absolute;width:94px;height:94px;border:1.5px dashed var(--line);border-radius:50%;background:var(--white);display:flex;align-items:center;justify-content:center}
.connector{position:absolute;border-color:var(--line);border-style:dashed}

/* portfolio */
.portfolio{position:absolute;left:0;top:1499px;width:1200px;height:341px}
.portfolio-intro{position:absolute;left:0;top:0;width:408px;height:341px;background:var(--blue);color:var(--white)}
.portfolio-intro h2{position:absolute;left:161px;top:65px;font-family:"Montserrat",sans-serif;font-size:17px;font-weight:600}
.portfolio-intro .rule{position:absolute;left:161px;top:94px;width:18px;height:2px;background:var(--white)}
.portfolio-intro p{position:absolute;left:161px;top:134px;width:205px;font-size:12px;line-height:19px}
.arrow-btn{position:absolute;top:237px;width:36px;height:36px;border:1.5px solid var(--white);display:flex;align-items:center;justify-content:center}
.portfolio-stage{position:absolute;left:408px;top:0;width:792px;height:341px;background:linear-gradient(135deg,#3a3f4c 0%,#1e2230 60%,#2c3244 100%)}
.case-card{position:absolute;top:56px;width:188px;height:239px}
.case-card .photo{position:absolute;inset:0}
.case-card .caption{position:absolute;left:0;right:0;bottom:0;height:36px;background:rgba(0,0,0,.55);display:flex;align-items:center;justify-content:center;font-family:"Montserrat",sans-serif;font-size:12px;font-weight:600;color:var(--white)}

/* partner strip */
.partners{position:absolute;left:0;top:1840px;width:1200px;height:100px}
.partner-badge{position:absolute;top:17px;height:65px;border:1px solid #e3e3e3;display:flex;align-items:center;justify-content:center}
.partner-badge span{display:block;width:90px;height:26px;background:#2a2a2a;border-radius:3px}

/* footer */
.site-footer{position:absolute;left:0;top:1940px;width:1200px;height:271px;background:var(--blue);color:var(--white)}
.contact-panel{position:absolute;left:0;top:0;width:408px;height:271px;background:var(--navy)}
.contact-panel h2{position:absolute;left:161px;top:35px;font-family:"Montserrat",sans-serif;font-size:17px;font-weight:600}
.field{position:absolute;left:161px;width:215px;background:var(--white);font-size:10px;color:#aaa;padding:7px 10px}
.submit{position:absolute;left:161px;top:203px;width:90px;height:33px;background:var(--orange);font-family:"Montserrat",sans-serif;font-size:11px;font-weight:700;display:flex;align-items:center;justify-content:center}
.footer-heading{position:absolute;top:41px;font-family:"Montserrat",sans-serif;font-size:11px;font-weight:700}
.footer-heading::after{content:"";position:absolute;left:0;top:21px;width:18px;height:1.5px;background:var(--white)}
.footer-list{position:absolute;list-style:none;font-size:10.5px;line-height:20px}
.footer-lines{position:absolute;font-size:10.5px;line-height:16px}
.copyright{position:absolute;left:668px;top:181px;font-size:10.5px}
</style>
</head>
<body>

<header class="site-header">
  <div class="brand"><span class="brand-mark"></span><span class="brand-name">MARENDO</span></div>
  <nav class="main-nav">
    <a href="#" style="left:573px">HOME</a>
    <a href="#" style="left:668px">ABOUT US</a>
    <a href="#" style="left:775px">SERVICES</a>
    <a href="#" style="left:884px">PORTFOLIO</a>
    <a href="#" style="left:1002px">CONTACT US</a>
  </nav>
</header>

<section class="hero">
  <div class="hero-photo" role="img" aria-label="Overhead photo of two business people shaking hands across a desk"></div>
  <h1 class="hero-title">We get you the results you have<br>only dreamt of reaching</h1>
  <p class="hero-text">Founded in April 2018, Marendo Advisers Limited (MAL) is an advisory consulting<br>firm specializing in engaging investors in business ventures in Tanzania.</p>
  <a class="btn btn-case">Case Studies</a>
  <a class="btn btn-services">Services</a>
</section>

<section class="about">
  <h2 class="section-title" style="top:65px">ABOUT US</h2>
  <p class="about-text">Founded in April 2018, Marendo Advisers Limited (MAL) is an advisory consulting firm specializing in engaging investors in business ventures in Tanzania. With extensive experience in construction, energy, oil and gas and the legal professions, our team assembles our expertise that allows foreign investors to set foot and flourish in the Tanzanian market.</p>
  <div class="about-more">experience in...</div>
  <div class="device" style="left:225px"><span class="device-cam"></span><span class="device-speaker"></span><div class="device-screen">South Africa</div></div>
  <div class="device" style="left:420px"><span class="device-cam"></span><span class="device-speaker"></span><div class="device-screen">Tanzania</div></div>
  <div class="device" style="left:615px"><span class="device-cam"></span><span class="device-speaker"></span><div class="device-screen">United Kingdom</div></div>
  <div class="device" style="left:809px"><span class="device-cam"></span><span class="device-speaker"></span><div class="device-screen">United States</div></div>
</section>

<section class="services">
  <h2 class="section-title" style="top:50px">SERVICES</h2>
  <span class="service-label" style="left:246px">Strategy Consultancy</span>
  <span class="service-label" style="left:422px">Programme Management</span>
  <span class="service-label" style="left:600px">Change Management</span>
  <span class="service-label" style="left:778px">Organizational Design</span>
  <span class="service-label" style="left:955px">Process Improvements</span>

  <div class="connector" style="left:246px;top:191px;width:709px;border-width:1.5px 0 0 0"></div>
  <div class="connector" style="left:600px;top:192px;height:293px;border-width:0 0 0 1.5px"></div>

  <div class="service-node" style="left:199px;top:145px">
    <svg width="50" height="44" viewBox="0 0 50 44"><rect x="16" y="2" width="18" height="13" rx="2" fill="#f7941d"/><circle cx="10" cy="20" r="5" fill="#1f3a5f"/><circle cx="40" cy="20" r="5" fill="#1f3a5f"/><path d="M3 36c0-7 3-10 7-10s7 3 7 10zM33 36c0-7 3-10 7-10s7 3 7 10z" fill="#1f3a5f"/><rect x="14" y="30" width="22" height="4" fill="#1f3a5f"/><rect x="22" y="34" width="6" height="8" fill="#1f3a5f"/></svg>
  </div>
  <div class="service-node" style="left:375px;top:145px">
    <svg width="50" height="44" viewBox="0 0 50 44"><rect x="3" y="4" width="44" height="28" rx="2" fill="none" stroke="#1f3a5f" stroke-width="3"/><rect x="10" y="18" width="5" height="10" fill="#f7941d"/><rect x="18" y="12" width="5" height="16" fill="#1f3a5f"/><rect x="26" y="20" width="5" height="8" fill="#f7941d"/><rect x="34" y="15" width="5" height="13" fill="#1f3a5f"/><rect x="20" y="32" width="10" height="6" fill="#1f3a5f"/><rect x="14" y="38" width="22" height="3" fill="#1f3a5f"/></svg>
  </div>
  <div class="service-node" style="left:553px;top:145px">
    <svg width="50" height="50" viewBox="0 0 50 50"><path d="M12 14a18 18 0 0 1 28 2" fill="none" stroke="#1f3a5f" stroke-width="3"/><path d="M38 36a18 18 0 0 1-28-2" fill="none" stroke="#1f3a5f" stroke-width="3"/><path d="M40 8v9h-9z" fill="#1f3a5f"/><path d="M10 42v-9h9z" fill="#1f3a5f"/><circle cx="25" cy="20" r="5" fill="#f7941d"/><rect x="17" y="27" width="16" height="8" rx="3" fill="#f7941d"/></svg>
  </div>
  <div class="service-node" style="left:731px;top:145px">
    <svg width="46" height="46" viewBox="0 0 46 46"><rect x="4" y="7" width="38" height="35" rx="4" fill="#1f3a5f"/><rect x="11" y="3" width="4" height="8" fill="#1f3a5f"/><rect x="31" y="3" width="4" height="8" fill="#1f3a5f"/><g fill="#f7941d"><rect x="10" y="17" width="7" height="6"/><rect x="20" y="17" width="7" height="6"/><rect x="30" y="17" width="7" height="6"/><rect x="10" y="27" width="7" height="6"/><rect x="20" y="27" width="7" height="6"/><rect x="30" y="27" width="7" height="6"/></g></svg>
  </div>
  <div class="service-node" style="left:908px;top:145px">
    <svg width="48" height="44" viewBox="0 0 48 44"><circle cx="30" cy="8" r="5" fill="#1f3a5f"/><path d="M25 15h9l3 14h-6l-2-7-6 5z" fill="#1f3a5f"/><rect x="6" y="22" width="18" height="11" fill="#f7941d"/><rect x="2" y="33" width="44" height="3" fill="#1f3a5f"/><rect x="6" y="36" width="3" height="7" fill="#1f3a5f"/><rect x="39" y="36" width="3" height="7" fill="#1f3a5f"/></svg>
  </div>

  <span class="service-label side" style="left:340px;top:331px">People Development</span>
  <div class="service-node" style="left:553px;top:291px">
    <svg width="50" height="44" viewBox="0 0 50 44"><circle cx="12" cy="14" r="5" fill="#1f3a5f"/><circle cx="38" cy="14" r="5" fill="#1f3a5f"/><path d="M3 34c0-8 4-13 9-13s9 5 9 13zM29 34c0-8 4-13 9-13s9 5 9 13z" fill="#1f3a5f"/><circle cx="25" cy="10" r="6" fill="#f7941d"/><path d="M14 40c0-10 5-15 11-15s11 5 11 15z" fill="#f7941d"/></svg>
  </div>

  <span class="service-label side" style="left:341px;top:477px">Funding Growth</span>
  <div class="service-node" style="left:553px;top:438px">
    <svg width="50" height="50" viewBox="0 0 50 50"><path d="M10 30a15 15 0 0 1 26-18" fill="none" stroke="#1f3a5f" stroke-width="5"/><path d="M40 20a15 15 0 0 1-26 18" fill="none" stroke="#f7941d" stroke-width="5"/><path d="M40 6v12h-12z" fill="#1f3a5f"/><path d="M10 44v-12h12z" fill="#f7941d"/></svg>
  </div>
</section>

<section class="portfolio">
  <div class="portfolio-intro">
    <h2>PORTFOLIO</h2>
    <span class="rule"></span>
    <p>Lorem ipsum dolor sit amet, consectetur adipiscing elit, sed do eiusmod tempor incididunt ut labore et</p>
    <span class="arrow-btn" style="left:162px"><svg width="10" height="12" viewBox="0 0 10 12"><path d="M7 1 2 6l5 5" fill="none" stroke="#fff" stroke-width="2"/></svg></span>
    <span class="arrow-btn" style="left:208px"><svg width="10" height="12" viewBox="0 0 10 12"><path d="m3 1 5 5-5 5" fill="none" stroke="#fff" stroke-width="2"/></svg></span>
  </div>
  <div class="portfolio-stage" role="img" aria-label="Dark photo of a businessman in a suit with a rising graph overlay">
    <div class="case-card" style="left:30px">
      <div class="photo" role="img" aria-label="Photo of two colleagues discussing a chart in an office" style="background:linear-gradient(160deg,#c9ced6 0%,#8c939e 60%,#4d535d 100%)"></div>
      <div class="caption">Lorem Ipsum Dolor</div>
    </div>
    <div class="case-card" style="left:239px">
      <div class="photo" role="img" aria-label="Photo of silhouetted team meeting in front of tall windows" style="background:linear-gradient(180deg,#b9c3c9 0%,#6d7378 45%,#2c2a28 100%)"></div>
      <div class="caption">Lorem Ipsum Dolor</div>
    </div>
    <div class="case-card" style="left:448px">
      <div class="photo" role="img" aria-label="Photo of a hand drawing a rising arrow graph" style="background:linear-gradient(150deg,#5b6a86 0%,#303a52 55%,#1c2233 100%)"></div>
      <div class="caption">Lorem Ipsum Dolor</div>
    </div>
  </div>
</section>

<section class="partners">
  <div class="partner-badge" style="left:203px;width:133px"><span></span></div>
  <div class="partner-badge" style="left:374px;width:129px"><span></span></div>
  <div class="partner-badge" style="left:540px;width:128px"><span></span></div>
  <div class="partner-badge" style="left:706px;width:128px"><span></span></div>
  <div class="partner-badge" style="left:871px;width:128px"><span></span></div>
</section>

<footer class="site-footer">
  <div class="contact-panel">
    <h2>CONTACT FORM</h2>
    <div class="field" style="top:66px;height:33px">Name*</div>
    <div class="field" style="top:106px;height:31px">Phone*</div>
    <div class="field" style="top:144px;height:47px">Comment*</div>
    <div class="submit">SUBMIT</div>
  </div>

  <h3 class="footer-heading" style="left:469px">NAVIGATION</h3>
  <ul class="footer-list" style="left:469px;top:80px">
    <li>Home</li><li>About Us</li><li>Services</li><li>Portfolio</li><li>Contact Us</li>
  </ul>

  <h3 class="footer-heading" style="left:668px">CONTACT</h3>
  <div class="footer-lines" style="left:668px;top:82px">Lorem Ipsum Dolor<br>Sit Amet Consect<br>Dolor Sit Amet<br>Consectetor</div>
  <div class="footer-lines" style="left:830px;top:82px">0012 555010200<br>info@marendoadvisers.example</div>
  <div class="copyright">Copyright 2018 Marendo Advisers All Rights Reserved</div>
</footer>

</body>
</html>
```